New Business Card Design For Re-Branded Company (New Logo)

We recently switched our DBA and had a new logo designed. We now need new business cards made around our new logo. We would like to stick with the color scheme in our logo: White, Orange, and Blue. We want to see original bold designs that reflect our position in the solar energy sector but we prefer simple over complicated.

We are curious about vertical designs so if you can translate your design onto a vertical layout we would be open to look at it. We especially like a few designs we have seen on here that are vertical with a black or very dark gray background. They have our logo on one side and then the normal vertical business card on the other side.

I have included a screenshot of one of the samples we like, labeled sample.jpg and a file we were given as an example of our logo on a dark background.

At the same time we are satisfied to stay with what we have always had in a horizontal format. If it's not a lot of extra work for you, designs that are submitted in both horizontal and vertical formats will be greatly appreciated.

Please submit your original, bold, clean designs for consideration. Contact us with any questions or comments that may arise.

Thank you and Good Luck,

KP

```html
<!DOCTYPE html>
<html lang="en">
<head>
<meta charset="UTF-8">
<title>Kestrel Power – Business Cards</title>
<link href="https://fonts.googleapis.com/css2?family=Montserrat:wght@500;600&family=Open+Sans:wght@600;700&display=swap" rel="stylesheet">
<style>
  :root {
    --blue: #2a7ab5;
    --orange: #e27a2f;
    --card-white: #f1f1f1;
    --paper: #e6e6e4;
    --deboss: #d6d6d6;
    --white: #ffffff;
  }
  * { margin: 0; padding: 0; box-sizing: border-box; }
  html, body { width: 1200px; height: 782px; overflow: hidden; }
  body { background: var(--paper); position: relative; font-family: "Open Sans", sans-serif; }

  .card { position: absolute; border-radius: 10px; overflow: hidden; box-shadow: 0 3px 10px rgba(0,0,0,0.15); }

  /* Horizontal front */
  .card-front { left: 135px; top: 340px; width: 550px; height: 310px; background: var(--blue); }
  .front-mark {
    position: absolute; left: 212px; top: 112px; width: 76px; height: 76px;
    border: 6px solid var(--orange); border-radius: 50%;
  }
  .front-name {
    position: absolute; left: 330px; top: 155px;
    transform: translate(-50%, -50%) rotate(-90deg);
    font-family: "Montserrat", sans-serif; font-weight: 500; font-size: 31px;
    letter-spacing: 1px; color: var(--white); white-space: nowrap;
  }
  .front-strip { position: absolute; left: 522px; top: 0; width: 28px; height: 310px; background: var(--white); }
  .front-strip-band { position: absolute; left: 0; top: 30px; width: 28px; height: 250px; background: var(--orange); }
  .front-web {
    position: absolute; left: 14px; top: 125px;
    transform: translate(-50%, -50%) rotate(-90deg);
    font-size: 11px; font-weight: 600; color: var(--white); white-space: nowrap; letter-spacing: 0.5px;
  }

  /* Vertical back */
  .card-back { left: 710px; top: 85px; width: 326px; height: 565px; background: var(--card-white); }
  .back-title {
    position: absolute; top: 36px; width: 100%; text-align: center;
    font-family: "Montserrat", sans-serif; font-weight: 600; font-size: 27px;
    color: var(--deboss); letter-spacing: 0.5px;
  }
  .back-mark {
    position: absolute; left: 128px; top: 160px; width: 70px; height: 70px;
    border-radius: 50%; background: var(--orange);
  }
  .back-name {
    position: absolute; top: 255px; width: 100%; text-align: center;
    font-family: "Montserrat", sans-serif; font-weight: 600; font-size: 27px;
    color: var(--blue); letter-spacing: 0.5px;
  }
  .person { position: absolute; top: 396px; width: 100%; text-align: center; }
  .person-name { font-size: 19px; font-weight: 700; color: var(--blue); line-height: 24px; }
  .person-role { font-size: 12px; font-weight: 700; color: var(--orange); letter-spacing: 0.5px; line-height: 16px; }
  .contact-icons { position: absolute; top: 452px; width: 100%; display: flex; justify-content: center; gap: 3px; }
  .contact-icons svg { width: 10px; height: 10px; }
  .contact-list { position: absolute; top: 468px; width: 100%; text-align: center; list-style: none; }
  .contact-list li { font-size: 13.5px; font-weight: 600; color: var(--blue); line-height: 17px; }
  .back-band { position: absolute; left: 0; bottom: 0; width: 100%; height: 28px; display: flex; }
  .band-end { width: 50px; background: var(--orange); }
  .band-mid { flex: 1; background: var(--blue); }
</style>
</head>
<body>
  <section class="card card-front">
    <div class="front-mark"></div>
    <div class="front-name">KESTREL POWER</div>
    <div class="front-strip">
      <div class="front-strip-band"></div>
      <div class="front-web">www.kestrelpower.com</div>
    </div>
  </section>

  <section class="card card-back">
    <div class="back-title">KESTREL POWER</div>
    <div class="back-mark"></div>
    <div class="back-name">KESTREL POWER</div>
    <div class="person">
      <div class="person-name">MARCUS HOLLIN</div>
      <div class="person-role">DIRECTOR</div>
    </div>
    <div class="contact-icons">
      <svg viewBox="0 0 10 10" aria-label="phone"><path d="M2 1 L4 3 L3 4 Q4 6 6 7 L7 6 L9 8 L8 9 Q3 9 1 2 Z" fill="none" stroke="#e27a2f" stroke-width="1"/></svg>
      <svg viewBox="0 0 10 10" aria-label="email"><rect x="1" y="2" width="8" height="6" fill="none" stroke="#e27a2f" stroke-width="1"/><path d="M1 2 L5 5.5 L9 2" fill="none" stroke="#e27a2f" stroke-width="1"/></svg>
      <svg viewBox="0 0 10 10" aria-label="web"><circle cx="5" cy="5" r="4" fill="none" stroke="#e27a2f" stroke-width="1"/><ellipse cx="5" cy="5" rx="1.8" ry="4" fill="none" stroke="#e27a2f" stroke-width="0.8"/><line x1="1" y1="5" x2="9" y2="5" stroke="#e27a2f" stroke-width="0.8"/></svg>
    </div>
    <ul class="contact-list">
      <li>505 0198 4471</li>
      <li>marcus@hollinmail.com</li>
      <li>www.kestrelpower.com</li>
    </ul>
    <div class="back-band">
      <div class="band-end"></div>
      <div class="band-mid"></div>
      <div class="band-end"></div>
    </div>
  </section>
</body>
</html>
```